そよかぜ日記(http://www.soyokaze-nikki.com/)から発刊した、Lumora電子書籍の表紙のデザインをコンペ形式で募集いたします。 電子書籍「庭仕事の始め方: 3年で畑を百坪に広げた家庭菜園術」(http://www.shoppomart.jp/exec/tenpo/item/Q77KTX3MZA/) の表紙をリニューアルします。 ファイル形式はjpeg(1600×2560px) 50MB未満でお願いします。 .psdファイルも一緒に納品してください(.pdfも可能)。 白地または非常に薄い背景色の表紙画像は、白い背景との区別がつかなくなる場合があります。幅の狭い (3 ~ 4 ピクセル) 薄灰色の枠線を追加して、表紙の境界を明確にしてください。 現在の表紙デザインに沿う必要はありません。書籍の魅力・内容をしっかりアピールしてくれるデザインを選んで採用させていただきます。 ご不明点や質問はお気軽にご相談ご相談ください。 たくさんのデザイナーの皆様からのご連絡・ご提案をお待ちしております。 |
タイトルが目につきやすいことと、シンプルですが軽くない感じのデザインが気に入りました。
皆さま、多くのご提案ありがとうございました。色々なタイプのデザインを拝見させていただくことができました。これから出版する電子書籍については、コンペで作ってもらおうと考えています。これからもよろしくお願いします。

```html
<!DOCTYPE html>
<html lang="ja">
<head>
<meta charset="utf-8">
<title>庭仕事の始め方</title>
<link rel="stylesheet" href="https://fonts.googleapis.com/css2?family=M+PLUS+Rounded+1c:wght@300;500&display=swap">
<style>
  :root {
    --cover-purple: #8b2f91;
    --glow-core: #c7a3d0;
    --glow-mid: #a566b0;
    --text-white: #ffffff;
  }
  html, body {
    margin: 0;
    padding: 0;
    overflow: hidden;
    background: var(--cover-purple);
  }
  .cover {
    position: relative;
    width: 749px;
    height: 1200px;
    overflow: hidden;
    background: var(--cover-purple);
    font-family: "M PLUS Rounded 1c", sans-serif;
    color: var(--text-white);
  }
  .title {
    margin: 0;
    font-weight: 300;
  }
  .title-column {
    position: absolute;
    display: flex;
    flex-direction: column;
    align-items: center;
    width: 140px;
  }
  .title-char {
    display: block;
    width: 140px;
    height: 132px;
    font-size: 120px;
    line-height: 132px;
    text-align: center;
  }
  .title-column--first {
    right: 30px;
    top: 40px;
  }
  .title-column--second {
    left: 20px;
    top: 105px;
  }
  .glow-art {
    position: absolute;
    left: 160px;
    top: 360px;
    width: 413px;
    height: 667px;
    border-radius: 40px;
    background: radial-gradient(ellipse at 50% 55%, var(--glow-core) 0%, var(--glow-mid) 45%, var(--cover-purple) 80%);
    filter: blur(6px);
  }
  .subtitle {
    position: absolute;
    left: 450px;
    top: 918px;
    margin: 0;
    font-size: 44px;
    font-weight: 500;
    line-height: 64px;
    white-space: nowrap;
  }
  .subtitle span {
    display: block;
  }
</style>
</head>
<body>
  <main class="cover">
    <div class="glow-art" role="img" aria-label="紫の背景にぼんやり光る柔らかな光のイラスト"></div>
    <h1 class="title" aria-label="庭仕事の始め方">
      <span class="title-column title-column--first">
        <span class="title-char">庭</span>
        <span class="title-char">仕</span>
        <span class="title-char">事</span>
        <span class="title-char">の</span>
      </span>
      <span class="title-column title-column--second">
        <span class="title-char">始</span>
        <span class="title-char">め</span>
        <span class="title-char">方</span>
      </span>
    </h1>
    <p class="subtitle">
      <span>3年で</span>
      <span>畑を百坪に</span>
      <span>広げた</span>
      <span>家庭菜園術</span>
    </p>
  </main>
</body>
</html>
```